New business card for Meridian Reach, a marketing company.

We need a new business card design. We would like it to be blue gray and white. We would like some movement but in a more subtle pattern than in the file we uploaded. We are a marketing company that connects brands with their target audiences - we make connections. We work in the New York Metro area with sophisticated clients. The card should feel modern, upscale and professional.

Target Market(s)

Businesses looking to grow their brands in tourism and nightlife. We work with liquor and beer companies and with Tourism bureaus and companies.

Industry/Entity Type

Marketing

Contact Information for Business Card

Would like a horizontal layout, two-sided. Would like the logo on the back with the tagline ' "bringing the right crowd to every brand" under the logo. On the front, we would like name, title, contact email, contact phone, website.

Font styles to use
Sans Serif

Colors
3377b5
85cae6
ffffff

Requirements
Must have
• Our logo. See attached. Otherwise, open to your ideas.
Should not have
• No colors we don't want - no reds/pinks/oranges please

```html
<!DOCTYPE html>
<html lang="en">
<head>
<meta charset="utf-8">
<title>Meridian Reach – Business Card</title>
<link href="https://fonts.googleapis.com/css2?family=Montserrat:wght@300;400;500&family=Lato:wght@400&display=swap" rel="stylesheet">
<style>
  :root {
    --brand-blue: #3377b5;
    --brand-sky: #85cae6;
    --edge-line: #a9c4e4;
    --white: #ffffff;
    --ink-grey: #555a60;
    --mark-grey: #9a9a9a;
    --rule-grey: #7d8086;
    --backdrop: #e9ecf0;
  }
  * { margin: 0; padding: 0; box-sizing: border-box; }
  html, body { width: 1200px; height: 1200px; overflow: hidden; }
  body {
    background: var(--backdrop);
    font-family: "Montserrat", sans-serif;
    position: relative;
  }
  .card {
    position: absolute;
    left: 180px;
    width: 840px;
    height: 480px;
    border-radius: 36px;
    overflow: hidden;
    background: var(--white);
    box-shadow: 0 6px 18px rgba(30, 40, 60, 0.18);
  }
  .card--back { top: 90px; }
  .card--front { top: 630px; }

  /* back side */
  .card__field { position: absolute; inset: 0; width: 100%; height: 100%; }
  .back-info {
    position: absolute;
    left: 360px;
    top: 150px;
    width: 440px;
    text-align: center;
    color: var(--white);
  }
  .back-info__name {
    font-weight: 400;
    font-size: 44px;
    letter-spacing: 1px;
    white-space: nowrap;
  }
  .back-info__web {
    font-size: 26px;
    font-weight: 500;
    letter-spacing: 0.5px;
    margin-top: 90px;
  }
  .back-info__tagline {
    font-family: "Lato", sans-serif;
    font-size: 17px;
    margin-top: 6px;
    white-space: nowrap;
  }

  /* front side */
  .vertical-mark {
    position: absolute;
    left: 105px;
    top: 240px;
    transform: translate(-50%, -50%) rotate(-90deg);
    white-space: nowrap;
    color: var(--mark-grey);
    font-size: 36px;
    font-weight: 300;
    letter-spacing: 1px;
  }
  .rule { position: absolute; background: var(--rule-grey); }
  .rule--vertical { left: 210px; top: 40px; width: 1.5px; height: 400px; }
  .rule--upper { left: 210px; top: 232px; width: 600px; height: 1.5px; }
  .rule--lower { left: 250px; top: 360px; width: 560px; height: 1.5px; }
  .person { position: absolute; left: 250px; top: 110px; color: var(--ink-grey); }
  .person__name { font-size: 40px; font-weight: 500; letter-spacing: 1px; }
  .person__title { font-size: 22px; font-weight: 400; letter-spacing: 1px; margin-top: 2px; }
  .contact { position: absolute; left: 300px; top: 262px; color: var(--ink-grey); list-style: none; }
  .contact__item { display: flex; align-items: center; gap: 14px; font-size: 28px; font-weight: 400; line-height: 42px; }
  .contact__icon { width: 22px; height: 22px; fill: var(--ink-grey); }
  .front-web {
    position: absolute; left: 300px; top: 390px;
    font-size: 28px; color: var(--ink-grey); letter-spacing: 0.5px;
  }
</style>
</head>
<body>

<section class="card card--back" aria-label="Card back">
  <svg class="card__field" viewBox="0 0 840 480" aria-hidden="true">
    <defs>
      <linearGradient id="backGradient" x1="0" y1="1" x2="1" y2="0">
        <stop offset="0" stop-color="#3377b5"/>
        <stop offset="1" stop-color="#85cae6"/>
      </linearGradient>
    </defs>
    <rect width="840" height="480" fill="url(#backGradient)"/>
    <path d="M0,0 L250,0 Q360,240 300,480 L0,480 Z" fill="var(--white)"/>
    <path d="M272,0 Q382,240 322,480" fill="none" stroke="var(--edge-line)" stroke-width="2" opacity="0.7"/>
  </svg>
  <div class="back-info">
    <p class="back-info__name">Meridian Reach</p>
    <p class="back-info__web">www.website.com</p>
    <p class="back-info__tagline">bringing the right crowd to every brand</p>
  </div>
</section>

<section class="card card--front" aria-label="Card front">
  <p class="vertical-mark">Meridian Reach</p>
  <span class="rule rule--vertical"></span>
  <span class="rule rule--upper"></span>
  <span class="rule rule--lower"></span>
  <div class="person">
    <p class="person__name">Name Of Person</p>
    <p class="person__title">Title Of Person</p>
  </div>
  <ul class="contact">
    <li class="contact__item">
      <svg class="contact__icon" viewBox="0 0 24 24" aria-hidden="true"><path d="M6.6 10.8a15.1 15.1 0 0 0 6.6 6.6l2.2-2.2a1 1 0 0 1 1-.25 11.4 11.4 0 0 0 3.6.57 1 1 0 0 1 1 1V20a1 1 0 0 1-1 1A17 17 0 0 1 3 4a1 1 0 0 1 1-1h3.5a1 1 0 0 1 1 1c0 1.25.2 2.45.57 3.57a1 1 0 0 1-.25 1z"/></svg>
      <span>+123 456 7890</span>
    </li>
    <li class="contact__item">
      <svg class="contact__icon" viewBox="0 0 24 24" aria-hidden="true"><path d="M2 5h20v14H2z M3.5 6.5 12 13l8.5-6.5" fill="none" stroke="#555a60" stroke-width="2"/></svg>
      <span>name@email.com</span>
    </li>
  </ul>
  <p class="front-web">www.website.com</p>
</section>

</body>
</html>
```